Packaging Design job - Product : Supplement for Travel Sickness

We need a packaging design for a travel sickness supplement called "VORALIN"

VORALIN It is a dietary supplement based on ginger which has properties fighting against motion sickness.

Ginger is a root used for many years for its beneficial effects on health. In addition to its stimulating and toning properties which help to resist fatigue, ginger is used as an adjuvant in case of nausea, vomiting and motion sickness. Ideal for pregnant women to combat certain disadvantages of pregnancy.

This product will be in blister form of 30 capsules. We need for this a packaging design for the box.Dimensions: 100 * 20 * 200 mm

We would like to see clean, modern and fresh designs.This should give the impression of professional products of pharmaceutical quality. You will also find attached the logo of our company.Ps : You can change the color of the logo

Mention to put on the box :

• Produit en France: Laboratoire CALDOR, 24 Rue des Tilleuls 41120 BRÉVAL
• Distribué au Maroc: KORAVITE 17 rue Idriss Benani 30000 FEZ MAROC
• Complément alimentaire, ce n'est pas un médicament
• Voie orale
• Tenir hors de portée des enfants
• Respectez la dose recommandée
• Ce produit ne remplace pas une alimentation variée

Mode d'utilisation (How to use) :

2 à 3 gélules 30 min avant de prendre le véhicule de transport
1 gélule par jour en cas de cure

Font styles to use
Serif
Sans Serif
Script

Requirements
Should not have
• Sales and other "must buy" "guaranteed" etc

```html
<!DOCTYPE html>
<html lang="en">
<head>
<meta charset="utf-8">
<title>VORALIN – Dietary Supplement Box Front</title>
<link rel="stylesheet" href="https://fonts.googleapis.com/css2?family=Montserrat:wght@600&family=Lato:wght@300;400&family=Courier+Prime:wght@700&display=swap">
<style>
  :root {
    --page-bg: #e9e9e9;
    --box-bg: #f0f0f0;
    --accent-yellow: #e3dc4d;
    --title-grey: #5e5e5e;
    --text-grey: #5a5a5a;
    --rule-grey: #6a6a6a;
    --count-green: #6cb43f;
    --brand-dark: #2a2a2a;
    --seal-red: #c9252c;
  }
  * { margin: 0; padding: 0; box-sizing: border-box; }
  html, body {
    width: 1200px;
    height: 1200px;
    overflow: hidden;
    background: var(--page-bg);
  }
  .box-front {
    position: absolute;
    left: 325px;
    top: 42px;
    width: 550px;
    height: 1115px;
    background: var(--box-bg);
    overflow: hidden;
  }
  .cap-arc {
    position: absolute;
    border-radius: 50%;
    background: var(--accent-yellow);
  }
  .cap-arc--top { left: 76px; top: -249px; width: 428px; height: 428px; }
  .cap-arc--bottom { left: 55px; top: 1059px; width: 438px; height: 438px; }
  .brand {
    position: absolute;
    left: 0; width: 580px;
    top: 70px;
    display: flex;
    justify-content: center;
    align-items: center;
    gap: 8px;
    font-family: "Montserrat", sans-serif;
    font-weight: 600;
    font-size: 25px;
    letter-spacing: 0.5px;
    color: var(--brand-dark);
  }
  .brand__dot {
    width: 12px; height: 12px;
    border-radius: 50%;
    background: var(--seal-red);
  }
  .product-name {
    position: absolute;
    left: 0; width: 566px;
    top: 407px;
    text-align: center;
    font-family: "Montserrat", sans-serif;
    font-weight: 600;
    font-size: 92px;
    line-height: 1;
    color: var(--title-grey);
    letter-spacing: 1px;
  }
  .category {
    position: absolute;
    left: 32px; width: 500px;
    top: 519px;
    text-align: center;
    white-space: nowrap;
    font-family: "Lato", sans-serif;
    font-weight: 300;
    font-size: 38px;
    line-height: 1;
    color: var(--text-grey);
  }
  .rule {
    position: absolute;
    left: 72px; width: 420px;
    height: 2px;
    background: var(--rule-grey);
  }
  .rule--upper { top: 566px; }
  .rule--lower { top: 671px; }
  .indication, .audience {
    position: absolute;
    left: 40px; width: 490px;
    text-align: center;
    font-family: "Courier Prime", monospace;
    font-weight: 700;
    font-size: 16.5px;
    line-height: 23px;
    color: var(--text-grey);
    white-space: nowrap;
  }
  .indication { top: 611px; }
  .audience { top: 682px; }
  .organic-seal {
    position: absolute;
    left: 176px; top: 822px;
    width: 134px; height: 136px;
  }
  .ginger-visual {
    position: absolute;
    left: 205px; top: 835px;
    width: 318px; height: 200px;
    border-radius: 45% 55% 40% 50%;
    background: radial-gradient(ellipse at 40% 65%, #efd79a 0%, #ddb878 45%, #b9a26a 70%, rgba(150,190,90,0.55) 85%, rgba(240,240,240,0) 100%);
  }
  .count {
    position: absolute;
    left: 22px; top: 997px;
    font-family: "Lato", sans-serif;
    font-weight: 400;
    font-size: 56px;
    line-height: 1;
    color: var(--count-green);
  }
  .count-unit, .basis {
    position: absolute;
    font-family: "Lato", sans-serif;
    font-weight: 400;
    font-size: 16px;
    line-height: 1;
    color: var(--text-grey);
    white-space: nowrap;
  }
  .count-unit { left: 17px; top: 1063px; }
  .basis { left: 371px; top: 1067px; }
</style>
</head>
<body>
  <main class="box-front">
    <div class="cap-arc cap-arc--top"></div>
    <div class="cap-arc cap-arc--bottom"></div>

    <div class="brand"><span class="brand__dot"></span>KORAVITE</div>

    <h1 class="product-name">VORALIN</h1>
    <p class="category">DIETARY SUPPLEMENT</p>
    <div class="rule rule--upper"></div>
    <p class="indication">use as an adjuvant in case of nausea,<br>vomiting and motion sickness.</p>
    <div class="rule rule--lower"></div>
    <p class="audience">Ideal for pregnant women</p>

    <div class="ginger-visual" role="img" aria-label="Photo of fresh ginger root with slices and green leaves"></div>

    <svg class="organic-seal" viewBox="0 0 134 136" role="img" aria-label="Organic certification seal">
      <circle cx="67" cy="68" r="62" fill="#ffffff" stroke="var(--seal-red)" stroke-width="4"/>
      <circle cx="67" cy="68" r="50" fill="none" stroke="var(--seal-red)" stroke-width="2.5"/>
    </svg>

    <div class="count">30</div>
    <div class="count-unit">CAPSULES</div>
    <div class="basis">BASED ON GINGER</div>
  </main>
</body>
</html>
```